Web Design Project

Need a web design for a website that provides senior corporate executives with leadership assessment and improvement guidance. The homepage has two purposes- 1) place for users to log in (primary purpose), and 2) marketing of the site.

The company is named Beacon 720, and it provides 360 degree leadership assessments for senior executives. In a nutshell, that means a person's co-workers, employees, customers, and bosses fill out a survey on how well the person does his or her job; and we tell him how well he or she is doing and how to improve.

The attached logo (360_logo) should serve as the inspiration for colors, and the website must use the logo. The homepage will mostly be used for logging in, so it should be simple, clean, and professional looking. See attached sketch.pdf for what we have in mind. The sketch is provided merely to give insight. We're not married to it. All text can be latinized jibberish in the design.

There is one important size constraint to keep in mind. The attached file (content_dimensions.pdf) specifies a content area that must be (width x height) 850 x 600 px.

Note that sketch.pdf portrays images, but please note these are merely placeholders. We will use screenshots of our application on the homepage, so any images you use in content area should be examples or suggestions.
Updates

Target Market(s)

Senior business executives from large companies in the manufacturing and energy sectors. Typically males aged 25 and older, white collar, upper class, with advanced degrees in business, engineering, and natural sciences.

Industry/Entity Type

It Company

Requirements
Must have
• See content_dimensions.pdf, which specifies the dimensions of the content area (850x600 px) (w x h). The the gutter and sides can expand beyond that, but the content area must be that specific size.

Note: The login panel must be within the content area.

Must use the attached logo (360_logo.png).
Should not have
• No Flash and no animated gifs. No photos of people.

```html
<!DOCTYPE html>
<html lang="en">
<head>
<meta charset="utf-8">
<title>Beacon 720 — Leadership Assessment</title>
<link href="https://fonts.googleapis.com/css2?family=Arimo:ital,wght@0,400;0,700;1,400&display=swap" rel="stylesheet">
<style>
  :root {
    --orange: #f7890f;
    --orange-title: #f38b14;
    --text-grey: #a9a9a9;
    --title-grey: #9a9a9a;
    --brand-grey: #8c8c8c;
    --content-bg: #f9f9f9;
    --footer-bg: #727272;
    --footer-text: #e6e6e6;
    --nav-top: #d9d9d9;
    --nav-bottom: #a4a4a4;
    --link-blue: #1f3f6e;
    --white: #ffffff;
  }
  * { box-sizing: border-box; margin: 0; padding: 0; }
  html, body { width: 1200px; height: 1055px; overflow: hidden; background: var(--white); }
  body { font-family: "Arimo", Arial, sans-serif; color: var(--text-grey); }

  .page {
    position: relative;
    width: 1024px;
    height: 900px;
    transform: scale(1.171875);
    transform-origin: 0 0;
  }
  .abs { position: absolute; }

  /* Header */
  .header-map {
    left: 265px; top: 0; width: 672px; height: 130px;
    background: radial-gradient(ellipse at 55% 40%, #e4e4e4 0%, #efefef 45%, #fafafa 80%, #ffffff 100%);
  }
  .brand-name {
    left: 140px; top: 100px; width: 144px; text-align: center;
    font-size: 20px; font-weight: 400; color: var(--brand-grey); white-space: nowrap;
  }
  .phone { right: 93px; top: 23px; font-size: 12px; font-style: italic; color: #8a8a8a; }

  .main-nav {
    left: 357px; top: 90px; width: 580px; height: 40px;
    display: flex;
    background: linear-gradient(to bottom, var(--nav-top), var(--nav-bottom));
  }
  .main-nav a {
    flex: none; display: flex; align-items: center; justify-content: center;
    color: var(--white); text-decoration: none; font-size: 16px;
    border-right: 1px solid rgba(255,255,255,0.35);
  }
  .main-nav a:last-child { border-right: none; }
  .main-nav a.is-active { font-weight: 700; }

  /* Content area */
  .content { left: 87px; top: 130px; width: 850px; height: 600px; background: var(--content-bg); }

  .login-frame {
    left: 88px; top: 155px; width: 250px; height: 240px;
    background: #f1f1f1; border-radius: 10px;
    box-shadow: 0 6px 6px -3px rgba(0,0,0,0.18);
  }
  .login-panel {
    left: 97px; top: 164px; width: 232px; height: 221px;
    background: var(--orange); border-radius: 6px; color: var(--white);
  }
  .login-title { position: absolute; left: 13px; top: 10px; font-size: 20px; font-weight: 700; }
  .field-label { position: absolute; left: 15px; font-size: 12px; font-weight: 700; }
  .field-input {
    position: absolute; height: 27px; background: var(--white);
    border: 1px solid #e6e6e6; border-radius: 3px;
  }
  .login-button {
    position: absolute; left: 12px; top: 178px; width: 206px; height: 33px;
    border-radius: 4px; background: linear-gradient(to bottom, #e2e2e2, #a9a9a9);
    color: var(--white); font-size: 12px; font-weight: 700;
    display: flex; align-items: center; justify-content: space-between; padding: 0 9px 0 8px;
  }

  .side-copy { left: 99px; top: 432px; width: 232px; font-size: 12px; line-height: 14.5px; }
  .read-more { left: 99px; top: 496px; font-size: 12px; font-style: italic; color: var(--link-blue); text-decoration: none; }

  .block-title { font-size: 24px; font-weight: 400; }
  .intro-title { left: 361px; top: 155px; color: var(--title-grey); }
  .intro-copy { left: 359px; top: 192px; width: 226px; font-size: 12px; line-height: 14.5px; }
  .chart-image { left: 605px; top: 155px; width: 331px; height: 215px;
    background: linear-gradient(135deg, #dfe3e8 0%, #f0ede6 40%, #c9b89a 75%, #e9e4da 100%); }

  .quote { left: 380px; top: 409px; width: 530px; font-size: 12px; line-height: 14.5px; font-style: italic; }

  .globe-image { left: 360px; top: 506px; width: 331px; height: 220px;
    background: radial-gradient(ellipse at 30% 45%, #2fb6d6 0%, #0a6f98 35%, #053650 70%, #02121c 100%); }
  .feature-title { left: 707px; top: 505px; color: var(--orange-title); }
  .feature-copy { left: 707px; top: 545px; width: 228px; font-size: 12px; line-height: 14.5px; }

  /* Footer */
  .footer { left: 0; top: 730px; width: 1024px; height: 170px; background: var(--footer-bg); }
  .copyright { position: absolute; left: 0; right: 0; top: 122px; text-align: center; font-size: 13px; color: var(--footer-text); }
</style>
</head>
<body>
<div class="page">

  <header>
    <div class="abs header-map" role="img" aria-label="Faint grey world map background"></div>
    <div class="abs brand-name">Beacon 720</div>
    <div class="abs phone">1-000-000-0000</div>
    <nav class="abs main-nav">
      <a href="#" style="width:140px">About</a>
      <a href="#" style="width:140px">Faq</a>
      <a href="#" class="is-active" style="width:145px">Help</a>
      <a href="#" style="width:155px">Contact</a>
    </nav>
  </header>

  <main>
    <div class="abs content"></div>

    <div class="abs login-frame"></div>
    <form class="abs login-panel">
      <div class="login-title">Login</div>
      <div class="field-label" style="top:47px">Name</div>
      <div class="field-input" style="left:14px; top:68px; width:205px"></div>
      <div class="field-label" style="top:108px">Password</div>
      <div class="field-input" style="left:13px; top:127px; width:205px"></div>
      <div class="login-button">
        <span>Login</span>
        <svg width="14" height="14" viewBox="0 0 14 14" aria-hidden="true">
          <circle cx="7" cy="7" r="7" fill="#5a5a5a"/>
          <path d="M5.3 4 L10 7 L5.3 10 Z" fill="#ffffff"/>
        </svg>
      </div>
    </form>

    <p class="abs side-copy">Lorem ipsum dolor sit amet, consectetur adipiscing elit. Sed lacinia feugiat massa, quis suscipit magna vehicula ac. Curabitur congue varius velit laoreet laoreet.</p>
    <a class="abs read-more" href="#">read more...</a>

    <h2 class="abs block-title intro-title">Title Here</h2>
    <p class="abs intro-copy">Lorem ipsum dolor sit amet, consectetur adipiscing elit. Sed lacinia feugiat massa, quis suscipit magna vehicula ac. Curabitur congue varius velit laoreet laoreet. Vestibulum ante ipsum primis in faucibus orci luctus et ultrices posuere cubilia Curae; Nullam sodales metus non turpis ullamcorper et lacinia urna tincidunt. Lorem ipsum dolor sit amet, consectetur adipiscing elit. Sed lacinia feugiat massa, quis suscipit magna vehicula ac.</p>
    <div class="abs chart-image" role="img" aria-label="Photo of printed sales reports with pie and bar charts"></div>

    <p class="abs quote">Lorem ipsum dolor sit amet, consectetur adipiscing elit. Sed lacinia feugiat massa, quis suscipit magna vehicula ac. Curabitur congue varius velit laoreet laoreet. Vestibulum ante ipsum primis in faucibus orci luctus et ultrices posuere cubilia Curae; Nullam sodales metus non turpis ullamcorper et lacinia urna tincidunt. Lorem ipsum dolor sit amet, consectetur adipiscing elit.</p>

    <div class="abs globe-image" role="img" aria-label="Blue abstract image of a wireframe globe with motion light"></div>
    <h2 class="abs block-title feature-title">Title Here</h2>
    <p class="abs feature-copy">Lorem ipsum dolor sit amet, consectetur adipiscing elit. Sed lacinia feugiat massa, quis suscipit magna vehicula ac. Curabitur congue varius velit laoreet laoreet. Vestibulum ante ipsum primis in faucibus orci luctus et ultrices posuere cubilia Curae; Nullam sodales metus non turpis ullamcorper et lacinia urna tincidunt.</p>
  </main>

  <footer class="abs footer">
    <p class="copyright">© 2013 Beacon 720</p>
  </footer>

</div>
</body>
</html>
```